TalkBloom - Language Coaching Services

Sleek, innovative, trendy design for Language Coaching business.

TalkBloom is a new UK based company that provides Language Coaching services. We offer highly personalized on-line and face to face language courses. We also impart learning techniques workshops based on the latest neuroscience research for second-language acquisition.

Target Market(s)

Industry/Entity Type

Consulting

Contact Information for Business Card

TalkBloom
DaniraQT@talkbloom.co.uk
TalkBloom.co.uk
London, UK

Font styles to use
Sans Serif

```html
<!DOCTYPE html>
<html lang="en">
<head>
<meta charset="utf-8">
<title>TalkBloom Business Card</title>
<link rel="stylesheet" href="https://fonts.googleapis.com/css2?family=Lato:wght@400;700&family=Montserrat:wght@400;500;700&display=swap">
<style>
  :root {
    --page-bg: #ececec;
    --card-white: #ffffff;
    --brand-blue: #0a8fce;
    --brand-deep: #0b72ae;
    --brand-sky: #17a8e0;
    --ink: #222222;
    --shadow: 0 4px 10px rgba(0, 0, 0, 0.28);
  }
  * { margin: 0; padding: 0; box-sizing: border-box; }
  html, body { width: 1200px; height: 900px; overflow: hidden; }
  body { background: var(--page-bg); position: relative; font-family: "Lato", sans-serif; }

  .card { position: absolute; box-shadow: var(--shadow); overflow: hidden; }

  .card-front { left: 330px; top: 90px; width: 555px; height: 343px; background: var(--card-white); }
  .card-back {
    left: 330px; top: 470px; width: 559px; height: 342px;
    background: linear-gradient(135deg, var(--brand-sky) 0%, var(--brand-blue) 55%, var(--brand-deep) 100%);
  }

  .brand-circle {
    position: absolute; border-radius: 50%; border: 8px solid var(--brand-blue);
  }
  .card-front .brand-circle { left: 104px; top: 22px; width: 108px; height: 108px; }
  .card-back .brand-circle { left: 216px; top: 84px; width: 128px; height: 128px; border-color: var(--card-white); border-width: 9px; }

  .wordmark {
    position: absolute; font-family: "Montserrat", sans-serif; font-weight: 500;
    letter-spacing: 1px; line-height: 1; white-space: nowrap;
  }
  .card-front .wordmark { left: 22px; top: 140px; font-size: 41px; color: var(--brand-blue); }
  .card-back .wordmark { left: 0; width: 100%; text-align: center; top: 222px; font-size: 45px; color: var(--card-white); }

  .holder { position: absolute; right: 27px; top: 36px; text-align: right; }
  .holder-name { font-family: "Montserrat", sans-serif; font-size: 20px; color: var(--brand-blue); letter-spacing: 0.5px; }
  .holder-name strong { font-weight: 700; }
  .holder-name span { font-weight: 400; }
  .holder-role { font-size: 15px; color: var(--ink); margin-top: 2px; }

  .contact-list { position: absolute; left: 26px; top: 256px; list-style: none; font-size: 15.5px; color: var(--ink); }
  .contact-list li { display: flex; align-items: center; height: 20px; }
  .contact-list svg { width: 12px; height: 12px; margin-right: 4px; fill: var(--brand-blue); }

  .office { position: absolute; right: 27px; top: 281px; text-align: right; font-size: 15.5px; line-height: 20px; }
  .office-name { color: var(--brand-blue); }
  .office-city { color: var(--ink); }
</style>
</head>
<body>
  <section class="card card-front">
    <div class="brand-circle"></div>
    <div class="wordmark">TALKBLOOM</div>

    <div class="holder">
      <div class="holder-name"><strong>ELLIOT</strong> <span>MARSH</span></div>
      <div class="holder-role">Managing Director</div>
    </div>

    <ul class="contact-list">
      <li>
        <svg viewBox="0 0 12 12" aria-hidden="true"><path d="M1 4c0-2 2-3 5-3s5 1 5 3l-2 1-1-2H4L3 5zM3 6h6l2 5H1z"/></svg>
        044 555 0199
      </li>
      <li>
        <svg viewBox="0 0 12 12" aria-hidden="true"><rect x="0.5" y="2" width="11" height="8"/><path d="M0.5 2.5 6 7l5.5-4.5" fill="none" stroke="#fff" stroke-width="1"/></svg>
        DaniraQT@talkbloom.co.uk
      </li>
      <li>
        <svg viewBox="0 0 12 12" aria-hidden="true"><circle cx="6" cy="6" r="5.5"/><path d="M0.5 6h11M6 0.5c-3 3-3 8 0 11M6 0.5c3 3 3 8 0 11" fill="none" stroke="#fff" stroke-width="0.8"/></svg>
        www.TalkBloom.co.uk
      </li>
    </ul>

    <div class="office">
      <div class="office-name">TALKBLOOM</div>
      <div class="office-city">London, UK</div>
    </div>
  </section>

  <section class="card card-back">
    <div class="brand-circle"></div>
    <div class="wordmark">TALKBLOOM</div>
  </section>
</body>
</html>
```